loyalty card design needed

Inner city Coffee shop/cafe- we need a loyalty card that will stand out in wallets.
Ideally we are wanting up to 4 rows of 10 sign boxes.

needs a note on it to say tenth coffee is free.

Target Market(s)

business people

Industry/Entity Type

Cafe

Contact Information for Business Card

LANTERN ROAST
47 Pelling Street
HOBART TASMANIA 7000
phone 03 62915384
www.lanternroast.com.au

Logo Text

LANTERN ROAST

Logo styles of interest
Wordmark Logo
Requirements
Must have
• Ideally we are wanting up to 4 rows of 10 sign boxes.

needs a note on it to say tenth coffee is free

colours as suggested in file upload
Nice to have
• really stand out form the rest of cards in a customers wallet.

```html
<!DOCTYPE html>
<html lang="en">
<head>
<meta charset="utf-8">
<title>Lantern Roast – Loyalty Card</title>
<link rel="stylesheet" href="https://fonts.googleapis.com/css2?family=Arimo:wght@700&family=Jost:wght@400;500;600&display=swap">
<style>
  :root {
    --stage: #ededed;
    --red-top: #d0103f;
    --red-bottom: #d6465a;
    --yellow-top: #dcde3a;
    --yellow-bottom: #e2df5c;
    --lime: #d6da45;
    --ink: #111111;
    --paper: #ffffff;
    --shadow: rgba(0,0,0,0.45);
  }
  * { box-sizing: border-box; margin: 0; padding: 0; }
  html, body { width: 1200px; height: 1000px; overflow: hidden; }
  body { background: var(--stage); position: relative; font-family: "Jost", sans-serif; }

  .card { position: absolute; width: 729px; height: 420px; box-shadow: 5px 5px 6px var(--shadow); overflow: hidden; }

  /* Front */
  .card--front { left: 78px; top: 57px; }
  .front__top { position: absolute; left: 0; top: 0; width: 100%; height: 235px;
    background: linear-gradient(to bottom, var(--red-top), var(--red-bottom)); }
  .front__rule { position: absolute; left: 0; top: 235px; width: 100%; height: 11px; background: var(--ink); }
  .front__bottom { position: absolute; left: 0; top: 246px; width: 100%; height: 174px;
    background: linear-gradient(to bottom, var(--yellow-top), var(--yellow-bottom)); }
  .brand-plate { position: absolute; left: 210px; top: 196px; width: 309px; height: 46px;
    background: var(--yellow-top); display: flex; align-items: center; justify-content: center; }
  .brand-name { font-family: "Arimo", sans-serif; font-weight: 700; font-size: 23px; color: var(--ink); letter-spacing: 0.2px; }
  .contact { position: absolute; left: 0; width: 100%; text-align: center; color: var(--ink);
    font-size: 15px; font-weight: 500; letter-spacing: 0.3px; line-height: 20px; }
  .contact--address { top: 257px; }
  .contact--phone { top: 309px; }
  .contact--web { top: 330px; }
  .contact svg { vertical-align: -3px; margin-right: 6px; }

  /* Back */
  .card--back { left: 393px; top: 522px; background: var(--paper); }
  .banner { position: absolute; left: 39px; top: 40px; }
  .banner__text { position: absolute; left: 39px; top: 40px; width: 649px; height: 52px;
    display: flex; align-items: center; justify-content: center;
    font-size: 28px; font-weight: 600; color: var(--paper); letter-spacing: 9px; }
  .banner__text .free { color: var(--yellow-top); margin-left: 14px; }
  .stamps { position: absolute; left: 40px; top: 116px; display: grid;
    grid-template-columns: repeat(10, 51px); column-gap: 15.3px; row-gap: 18px; }
  .stamp { width: 51px; height: 51px; background: var(--lime); padding: 4px; }
  .stamp span { display: flex; width: 100%; height: 100%; background: var(--paper); border-radius: 11px;
    align-items: center; justify-content: center; color: var(--lime); font-weight: 600; font-size: 25px; }
</style>
</head>
<body>
  <section class="card card--front">
    <div class="front__top"></div>
    <div class="front__rule"></div>
    <div class="front__bottom"></div>
    <div class="brand-plate"><span class="brand-name">LANTERN ROAST</span></div>
    <p class="contact contact--address">47 PELLING STREET<br>HOBART TASMANIA 7000</p>
    <p class="contact contact--phone">
      <svg width="14" height="16" viewBox="0 0 14 16" aria-hidden="true"><path d="M4 1 L6.5 1 L7 5 L5.2 6 Q6 10 8 11.5 L9.5 10.3 L12.5 12.5 L11.5 15 Q5 15 2.5 8 Q1.5 3.5 4 1 Z" fill="var(--red-top)"/></svg>03 62915384</p>
    <p class="contact contact--web">
      <svg width="16" height="16" viewBox="0 0 16 16" aria-hidden="true"><circle cx="8" cy="8" r="7" fill="none" stroke="var(--red-top)" stroke-width="2"/><path d="M1 8 H15 M8 1 Q4 8 8 15 M8 1 Q12 8 8 15" fill="none" stroke="var(--red-top)" stroke-width="1.4"/></svg>WWW.LANTERNROAST.COM.AU</p>
  </section>

  <section class="card card--back">
    <svg class="banner" width="650" height="72" viewBox="0 0 650 72" aria-hidden="true">
      <defs>
        <linearGradient id="bannerRed" x1="0" y1="0" x2="0" y2="1">
          <stop offset="0" stop-color="var(--red-top)"/>
          <stop offset="1" stop-color="var(--red-bottom)"/>
        </linearGradient>
      </defs>
      <path d="M0 0 H628 Q649 0 649 21 V52 H627 L623 71 L619 52 H22 Q0 52 0 30 Z" fill="url(#bannerRed)"/>
    </svg>
    <div class="banner__text">10th Coffee<span class="free">FREE</span></div>
    <div class="stamps">
      <div class="stamp"><span>1</span></div><div class="stamp"><span>2</span></div><div class="stamp"><span>3</span></div><div class="stamp"><span>4</span></div><div class="stamp"><span>5</span></div><div class="stamp"><span>6</span></div><div class="stamp"><span>7</span></div><div class="stamp"><span>8</span></div><div class="stamp"><span>9</span></div><div class="stamp"><span>10</span></div>
      <div class="stamp"><span>1</span></div><div class="stamp"><span>2</span></div><div class="stamp"><span>3</span></div><div class="stamp"><span>4</span></div><div class="stamp"><span>5</span></div><div class="stamp"><span>6</span></div><div class="stamp"><span>7</span></div><div class="stamp"><span>8</span></div><div class="stamp"><span>9</span></div><div class="stamp"><span>10</span></div>
      <div class="stamp"><span>1</span></div><div class="stamp"><span>2</span></div><div class="stamp"><span>3</span></div><div class="stamp"><span>4</span></div><div class="stamp"><span>5</span></div><div class="stamp"><span>6</span></div><div class="stamp"><span>7</span></div><div class="stamp"><span>8</span></div><div class="stamp"><span>9</span></div><div class="stamp"><span>10</span></div>
      <div class="stamp"><span>1</span></div><div class="stamp"><span>2</span></div><div class="stamp"><span>3</span></div><div class="stamp"><span>4</span></div><div class="stamp"><span>5</span></div><div class="stamp"><span>6</span></div><div class="stamp"><span>7</span></div><div class="stamp"><span>8</span></div><div class="stamp"><span>9</span></div><div class="stamp"><span>10</span></div>
    </div>
  </section>
</body>
</html>
```